Industry: Christian Ministry using Magic, Music and Multimedia to teach gospel

“Lanternfold Ministries brings the Gospel of Jesus Christ, with heart-seeking, biblical accuracy
through live, entertainment-based evangelistic Celebrations."

We are a service that wants to partner with christian religious institutions and churches to teach biblical gospel in a fun and entertaining way using magic.

Design inspiration: https://www.quillmarshwonders.example

DO NOT CONTACT ME PRIVATELY. IT WILL BE IGNORED.

Important:
1. Use only royalty free graphics
2. Use only google fonts
3. A clean, linear layout
4. Do not include search

PAGES

1. Home
2. Shows & Skylark
3. About Lanternfold
4. Media
5. Contact & Support

Color pallets
#0053E0
#FF2500
#ffffff

Please see attachment for more detail

Target Market(s)

Churches and christian schools

Industry/Entity Type

magic, entertainment, christianity

Number of Pages Required

5+ page

Colors
0054AA
0677BA
7BADD7
CADEEF
E8F1F8

Requirements
Should not have
• - search bar

```html
<!DOCTYPE html>
<html lang="en">
<head>
<meta charset="utf-8">
<title>Media | Lanternfold Ministries</title>
<link rel="stylesheet" href="https://fonts.googleapis.com/css2?family=Montserrat:wght@400;500;600;700&display=swap">
<style>
:root{
  --blue:#0053E0;
  --red:#FF2500;
  --white:#ffffff;
  --ink:#2b2b2b;
  --muted:#666666;
  --footer:#0d0d0d;
}
*{box-sizing:border-box;margin:0;padding:0}
html,body{width:1200px;height:2979px;overflow:hidden}
body{font-family:'Montserrat',sans-serif;background:var(--white);color:var(--ink)}
a{color:inherit;text-decoration:none}

.hero{position:relative;height:410px;overflow:hidden}
.hero-photo{position:absolute;inset:0;background:
  radial-gradient(ellipse at 55% 40%,#5a3a2e 0%,#2a1a18 40%,#0c0808 75%),#111}
.hero-photo::after{content:"";position:absolute;left:0;right:0;bottom:0;height:130px;
  background:linear-gradient(180deg,rgba(60,40,35,0) 0%,rgba(70,50,40,.8) 100%)}
.site-header{position:absolute;top:0;left:0;right:0;height:120px;display:flex;justify-content:space-between;align-items:flex-start;padding:0 111px}
.brand{margin-top:26px;color:var(--white);font-weight:600;line-height:1}
.brand .name{display:block;font-size:42px;letter-spacing:.5px}
.brand .sub{display:block;font-size:30px;margin-top:6px}
.main-nav{display:flex;gap:24px;margin-top:54px}
.main-nav a{color:var(--white);font-weight:600;font-size:17px}
.main-nav a.active{color:var(--red)}
.page-title{position:absolute;left:109px;top:194px;color:var(--white);font-size:52px;font-weight:700;letter-spacing:.5px}

.posts{height:2185px;padding-top:65px}
.post{display:flex;width:978px;margin:0 auto 39px;height:353px}
.post-media{width:460px;height:353px;padding:6px;background:var(--white);box-shadow:0 0 6px rgba(0,0,0,.25);flex:none}
.post-media div{width:100%;height:100%}
.m1{background:linear-gradient(180deg,#c9c6bd 0%,#8a8478 50%,#3a3530 100%)}
.m2{background:linear-gradient(180deg,#b7bcc0 0%,#4a4a4a 45%,#b58a4a 100%)}
.m3{background:radial-gradient(ellipse at 60% 45%,#2a34b8 0%,#0a1470 55%,#060a30 100%)}
.m4{background:radial-gradient(ellipse at 40% 40%,#33356a 0%,#0d1030 70%)}
.m5{background:linear-gradient(180deg,#d8d6cc 0%,#6a6a70 40%,#1e2440 100%)}
.post-body{margin-left:60px;width:458px}
.post-cat{margin-top:12px;color:var(--blue);font-size:17px;text-transform:uppercase;font-weight:500}
.post-title{margin-top:8px;font-size:28px;font-weight:500;line-height:33px;color:var(--ink)}
.post-meta{margin-top:14px;font-size:17px;color:var(--ink);display:flex;align-items:center;gap:4px}
.post-meta svg{width:15px;height:15px}
.post-meta .sep{margin:0 8px}
.post-text{margin-top:28px;font-size:16px;line-height:26.6px;color:var(--muted)}
.more{display:block;width:161px;height:52px;margin:41px auto 0;border-radius:26px;background:var(--red);color:var(--white);font-weight:700;font-size:18px;text-align:center;line-height:52px}

.site-footer{height:384px;background:var(--footer);color:var(--white);position:relative}
.footer-brand{position:absolute;left:111px;top:105px;font-weight:600;line-height:1}
.footer-brand .name{display:block;font-size:60px}
.footer-brand .sub{display:block;font-size:42px;margin-top:10px}
.footer-col{position:absolute;top:60px}
.footer-col h3{font-size:18px;font-weight:600;margin-bottom:18px}
.footer-col li{list-style:none;font-size:16px;line-height:30px;display:flex;align-items:center;gap:8px}
.footer-col li svg{width:14px;height:14px}
.col-links{left:500px}
.col-contact{left:757px;top:60px}
.col-contact li{line-height:34px}
.rule{position:absolute;left:111px;right:111px;top:282px;border-top:1px solid #444}
.copyright{position:absolute;left:111px;top:320px;font-size:16px}
.social{position:absolute;right:112px;top:308px;width:44px;height:44px;border:1px solid #888;border-radius:50%;display:flex;align-items:center;justify-content:center}
.social span{width:10px;height:10px;border-radius:50%;background:var(--red)}
</style>
</head>
<body>
<header class="hero">
  <div class="hero-photo" role="img" aria-label="Live worship show on stage with band and singer before a seated audience"></div>
  <div class="site-header">
    <a class="brand" href="#"><span class="name">Lanternfold</span><span class="sub">Ministries</span></a>
    <nav class="main-nav">
      <a href="#">Home</a><a href="#">Shows &amp; Skylark</a><a href="#">About Lanternfold</a><a class="active" href="#">Media</a><a href="#">Contact &amp; Support</a>
    </nav>
  </div>
  <h1 class="page-title">MEDIA</h1>
</header>

<main class="posts">
  <article class="post">
    <div class="post-media"><div class="m1" role="img" aria-label="Audience in a church hall watching a projected presentation"></div></div>
    <div class="post-body">
      <p class="post-cat">Tips and Tools</p>
      <h2 class="post-title">Duis aute irure dolor in repreheln derit in voluptate velit</h2>
      <p class="post-meta"><svg viewBox="0 0 16 16"><rect x="1" y="3" width="14" height="12" fill="none" stroke="#FF2500" stroke-width="2"/><rect x="1" y="3" width="14" height="4" fill="#FF2500"/><rect x="4" y="0" width="2" height="4" fill="#FF2500"/><rect x="10" y="0" width="2" height="4" fill="#FF2500"/></svg>22/04/2023<span class="sep">|</span><svg viewBox="0 0 16 16"><rect x="1" y="3" width="14" height="12" fill="none" stroke="#FF2500" stroke-width="2"/><rect x="1" y="3" width="14" height="4" fill="#FF2500"/><rect x="4" y="0" width="2" height="4" fill="#FF2500"/><rect x="10" y="0" width="2" height="4" fill="#FF2500"/></svg>Admin</p>
      <p class="post-text">Lorem ipsum dolor sit amet, consectetur adipiscing elit, sed do eiusmod tempor incididunt ut labore et dolore magna aliqua. Ut enim ad minim veniam, quis nostrud exercitation ullamco laboris nisi ut aliquip ex ea comodo consequat. Duis aute irure dolor in reprehenderit in vol uptate velit esse cillum dolore eu fug.</p>
    </div>
  </article>
  <article class="post">
    <div class="post-media"><div class="m2" role="img" aria-label="Two volunteers standing behind donated canned food"></div></div>
    <div class="post-body">
      <p class="post-cat">Tips and Tools</p>
      <h2 class="post-title">Duis aute irure dolor in repreheln derit in voluptate velit</h2>
      <p class="post-meta"><svg viewBox="0 0 16 16"><rect x="1" y="3" width="14" height="12" fill="none" stroke="#FF2500" stroke-width="2"/><rect x="1" y="3" width="14" height="4" fill="#FF2500"/><rect x="4" y="0" width="2" height="4" fill="#FF2500"/><rect x="10" y="0" width="2" height="4" fill="#FF2500"/></svg>22/04/2023<span class="sep">|</span><svg viewBox="0 0 16 16"><rect x="1" y="3" width="14" height="12" fill="none" stroke="#FF2500" stroke-width="2"/><rect x="1" y="3" width="14" height="4" fill="#FF2500"/><rect x="4" y="0" width="2" height="4" fill="#FF2500"/><rect x="10" y="0" width="2" height="4" fill="#FF2500"/></svg>Admin</p>
      <p class="post-text">Lorem ipsum dolor sit amet, consectetur adipiscing elit, sed do eiusmod tempor incididunt ut labore et dolore magna aliqua. Ut enim ad minim veniam, quis nostrud exercitation ullamco laboris nisi ut aliquip ex ea comodo consequat. Duis aute irure dolor in reprehenderit in vol uptate velit esse cillum dolore eu fug.</p>
    </div>
  </article>
  <article class="post">
    <div class="post-media"><div class="m3" role="img" aria-label="Performer on a blue-lit stage holding a book"></div></div>
    <div class="post-body">
      <p class="post-cat">Tips and Tools</p>
      <h2 class="post-title">Duis aute irure dolor in repreheln derit in voluptate velit</h2>
      <p class="post-meta"><svg viewBox="0 0 16 16"><rect x="1" y="3" width="14" height="12" fill="none" stroke="#FF2500" stroke-width="2"/><rect x="1" y="3" width="14" height="4" fill="#FF2500"/><rect x="4" y="0" width="2" height="4" fill="#FF2500"/><rect x="10" y="0" width="2" height="4" fill="#FF2500"/></svg>22/04/2023<span class="sep">|</span><svg viewBox="0 0 16 16"><rect x="1" y="3" width="14" height="12" fill="none" stroke="#FF2500" stroke-width="2"/><rect x="1" y="3" width="14" height="4" fill="#FF2500"/><rect x="4" y="0" width="2" height="4" fill="#FF2500"/><rect x="10" y="0" width="2" height="4" fill="#FF2500"/></svg>Admin</p>
      <p class="post-text">Lorem ipsum dolor sit amet, consectetur adipiscing elit, sed do eiusmod tempor incididunt ut labore et dolore magna aliqua. Ut enim ad minim veniam, quis nostrud exercitation ullamco laboris nisi ut aliquip ex ea comodo consequat. Duis aute irure dolor in reprehenderit in vol uptate velit esse cillum dolore eu fug.</p>
    </div>
  </article>
  <article class="post">
    <div class="post-media"><div class="m4" role="img" aria-label="Performer on stage amid a shower of falling confetti"></div></div>
    <div class="post-body">
      <p class="post-cat">Tips and Tools</p>
      <h2 class="post-title">Duis aute irure dolor in repreheln derit in voluptate velit</h2>
      <p class="post-meta"><svg viewBox="0 0 16 16"><rect x="1" y="3" width="14" height="12" fill="none" stroke="#FF2500" stroke-width="2"/><rect x="1" y="3" width="14" height="4" fill="#FF2500"/><rect x="4" y="0" width="2" height="4" fill="#FF2500"/><rect x="10" y="0" width="2" height="4" fill="#FF2500"/></svg>22/04/2023<span class="sep">|</span><svg viewBox="0 0 16 16"><rect x="1" y="3" width="14" height="12" fill="none" stroke="#FF2500" stroke-width="2"/><rect x="1" y="3" width="14" height="4" fill="#FF2500"/><rect x="4" y="0" width="2" height="4" fill="#FF2500"/><rect x="10" y="0" width="2" height="4" fill="#FF2500"/></svg>Admin</p>
      <p class="post-text">Lorem ipsum dolor sit amet, consectetur adipiscing elit, sed do eiusmod tempor incididunt ut labore et dolore magna aliqua. Ut enim ad minim veniam, quis nostrud exercitation ullamco laboris nisi ut aliquip ex ea comodo consequat. Duis aute irure dolor in reprehenderit in vol uptate velit esse cillum dolore eu fug.</p>
    </div>
  </article>
  <article class="post">
    <div class="post-media"><div class="m5" role="img" aria-label="Hall full of school children seated under colourful balloons"></div></div>
    <div class="post-body">
      <p class="post-cat">Tips and Tools</p>
      <h2 class="post-title">Duis aute irure dolor in repreheln derit in voluptate velit</h2>
      <p class="post-meta"><svg viewBox="0 0 16 16"><rect x="1" y="3" width="14" height="12" fill="none" stroke="#FF2500" stroke-width="2"/><rect x="1" y="3" width="14" height="4" fill="#FF2500"/><rect x="4" y="0" width="2" height="4" fill="#FF2500"/><rect x="10" y="0" width="2" height="4" fill="#FF2500"/></svg>22/04/2023<span class="sep">|</span><svg viewBox="0 0 16 16"><rect x="1" y="3" width="14" height="12" fill="none" stroke="#FF2500" stroke-width="2"/><rect x="1" y="3" width="14" height="4" fill="#FF2500"/><rect x="4" y="0" width="2" height="4" fill="#FF2500"/><rect x="10" y="0" width="2" height="4" fill="#FF2500"/></svg>Admin</p>
      <p class="post-text">Lorem ipsum dolor sit amet, consectetur adipiscing elit, sed do eiusmod tempor incididunt ut labore et dolore magna aliqua. Ut enim ad minim veniam, quis nostrud exercitation ullamco laboris nisi ut aliquip ex ea comodo consequat. Duis aute irure dolor in reprehenderit in vol uptate velit esse cillum dolore eu fug.</p>
    </div>
  </article>
  <a class="more" href="#">VIEW MORE</a>
</main>

<footer class="site-footer">
  <div class="footer-brand"><span class="name">Lanternfold</span><span class="sub">Ministries</span></div>
  <div class="footer-col col-links">
    <h3>Quick Links</h3>
    <ul><li>Home</li><li>Shows &amp; Skylark</li><li>About Lanternfold</li><li>Media</li><li>Contact &amp; Support</li></ul>
  </div>
  <div class="footer-col col-contact">
    <h3>Contact Us</h3>
    <ul>
      <li>Lanternfold Ministries Inc.</li>
      <li><svg viewBox="0 0 14 14"><path d="M7 0a5 5 0 0 0-5 5c0 4 5 9 5 9s5-5 5-9a5 5 0 0 0-5-5z" fill="#FF2500"/><circle cx="7" cy="5" r="2" fill="#0d0d0d"/></svg>Cedar Hollow, Georgia, USA</li>
      <li><svg viewBox="0 0 14 14"><path d="M3 0l3 3-2 2a9 9 0 0 0 5 5l2-2 3 3-2 3C6 14 0 8 0 2z" fill="#FF2500"/></svg>555-014-2870</li>
      <li><svg viewBox="0 0 14 14"><rect x="0" y="2" width="14" height="10" fill="#FF2500"/><path d="M0 2l7 6 7-6" fill="none" stroke="#0d0d0d" stroke-width="1.5"/></svg>Email Us</li>
    </ul>
  </div>
  <div class="rule"></div>
  <p class="copyright">Copyright © - 2023 Lanternfold Ministries Inc., All Rights Reserved</p>
  <a class="social" href="#" aria-label="Social page"><span></span></a>
</footer>
</body>
</html>
```